Business Card Re-Design/Update

We'd like to update out business cards. I've included our current "Style guide" which has the colour scheme of the organisation in it. I've also included the branding files with logos etc in them.

I've also included a copy of one of our existing cards so that you can see how ugly/dated they look. I'd like a fresh modern corporate look.

Target Market(s)

These are for our clients, potential clients, industry contacts - like all business cards

Contact Information for Business Card

Name
Position
Company Address - Level 1, 47 Garnet Lane, Toowong Qld 4066
Direct Phone
mobile
Email
Website -www.korvalnet.com.au
Logo

Colors

Designer to choose colors to be used in the design.

Requirements
Must have
• Main Logo
• Cards will need to be editable to be able to personalize them for each new employee.
Nice to have
• The MapOUT, HandOVER, UpKEEP would be okay to have if they can be sensibly and professionally added to the look without detracting from the main imagery.
• Maybe they could go on the back of the card? will leave this to your creative discretion as to whether/where they fit.
Should not have
• Should not have decorative or script fonts

```html
<!DOCTYPE html>
<html lang="en">
<head>
<meta charset="utf-8">
<title>korvalnet business card</title>
<link rel="stylesheet" href="https://fonts.googleapis.com/css2?family=Arimo:wght@400;700&display=swap">
<style>
  :root {
    --page: #e9e7e4;
    --card-dark: #2b2b2b;
    --card-light: #ffffff;
    --ink: #2a2a2a;
    --ink-soft: #4a4a4a;
    --brand-red: #c8161d;
    --wordmark-grey: #6e6e6e;
    --map-green: #5aa832;
    --hand-blue: #2a8ccf;
    --keep-magenta: #c2268f;
    --band-text: #bdbdbd;
  }
  * { margin: 0; padding: 0; box-sizing: border-box; }
  html, body { width: 1200px; height: 744px; overflow: hidden; }
  body {
    background: var(--page);
    font-family: "Arimo", Arial, sans-serif;
    display: flex;
    align-items: center;
    justify-content: center;
    gap: 60px;
  }
  .card {
    width: 500px;
    height: 286px;
    position: relative;
    box-shadow: 0 6px 18px rgba(0,0,0,0.18);
    overflow: hidden;
  }

  /* Front */
  .card--front {
    background: var(--card-dark);
    display: flex;
    align-items: center;
    justify-content: center;
    gap: 22px;
  }
  .front-mark {
    width: 74px;
    height: 74px;
    background: var(--brand-red);
  }
  .front-wordmark {
    font-size: 46px;
    font-weight: 400;
    letter-spacing: -0.5px;
    color: var(--wordmark-grey);
  }

  /* Back */
  .card--back {
    background: var(--card-light);
    display: flex;
    flex-direction: column;
  }
  .back-body {
    flex: 1;
    padding: 26px 30px 0 30px;
    color: var(--ink);
  }
  .brand {
    display: flex;
    align-items: center;
    gap: 10px;
  }
  .brand-mark {
    width: 26px;
    height: 26px;
    background: var(--brand-red);
  }
  .brand-name {
    font-size: 34px;
    font-weight: 400;
    letter-spacing: -0.5px;
    color: var(--ink);
    line-height: 1;
  }
  .person { margin: 10px 0 0 36px; }
  .person-name { font-size: 17px; font-weight: 400; }
  .person-role { font-size: 11px; color: var(--ink-soft); margin-top: 3px; }
  .contact {
    margin: 14px 0 0 0;
    font-size: 10.5px;
    line-height: 1.55;
    color: var(--ink);
  }
  .contact-row { display: flex; }
  .contact-row .col { width: 165px; }
  .contact-row .sep { width: 22px; text-align: center; }
  .band {
    height: 54px;
    background: var(--card-dark);
    display: flex;
    align-items: center;
    justify-content: space-around;
    padding: 0 40px;
  }
  .service {
    display: flex;
    align-items: center;
    gap: 6px;
    font-size: 14px;
    color: var(--band-text);
  }
  .service-dot { width: 11px; height: 11px; }
  .service--map .service-dot { background: var(--map-green); }
  .service--hand .service-dot { background: var(--hand-blue); }
  .service--keep .service-dot { background: var(--keep-magenta); }
  .service--map .accent { color: var(--map-green); }
  .service--hand .accent { color: var(--hand-blue); }
  .service--keep .accent { color: var(--keep-magenta); }
</style>
</head>
<body>
  <section class="card card--front" aria-label="Card front">
    <div class="front-mark"></div>
    <div class="front-wordmark">korvalnet</div>
  </section>

  <section class="card card--back" aria-label="Card back">
    <div class="back-body">
      <div class="brand">
        <div class="brand-mark"></div>
        <div class="brand-name">korvalnet</div>
      </div>
      <div class="person">
        <div class="person-name">Mara Ellison</div>
        <div class="person-role">Business Development Manager</div>
        <div class="contact">
          <div class="contact-row">
            <span class="col">M +61 (0)412 555 018</span><span class="sep">|</span><span>D +61 (0)7 3000 4416</span>
          </div>
          <div class="contact-row">
            <span class="col">P +61 (0)7 3000 4410</span><span class="sep">|</span><span>F +61 (0)7 3000 4403</span>
          </div>
          <div>E mellison@korvalnet.com.au</div>
          <div>Level 1, 47 Garnet Lane, Toowong Qld 4066</div>
        </div>
      </div>
    </div>
    <div class="band">
      <div class="service service--map"><span class="service-dot"></span><span><span class="accent">Map</span>OUT</span></div>
      <div class="service service--hand"><span class="service-dot"></span><span><span class="accent">Hand</span>OVER</span></div>
      <div class="service service--keep"><span class="service-dot"></span><span><span class="accent">Up</span>KEEP</span></div>
    </div>
  </section>
</body>
</html>
```